High End Personalized Functional Medicine in Women's Health

We are adding new and exciting personalized medicine services to our Women's Health Care practice focusing on health optimization and anti-aging as well as hormone replacement therapy and need a high end brochure to educate patients about these services. We would like to see a zen-like design that has feminine appeal. Our office colors are vibrant but soothing. We have utilized the concepts of feng shui to optimize our positive energy. The exterior of the building is peach and cream and these colors would blend with that energy The final design should communicate a sense that you can take control of your health and aging.
Updates

Target Market(s)

Females age 35-65 with annual income >$75000/year

Industry/Entity Type

Health And Wellness

Logo Text

Bright Path is the company name. Our sister company is Mesa Rio Ob/Gyn

Font styles to use
Serif

Colors

Designer to choose colors to be used in the design.

Requirements
Must have
• My project must have clean lines. I like a strong feminine appearance, not a fluffy curvy feminine look. Professional appearance, Brochure would be on thicker card stock. A strong front page that makes you want to open the brochure
Nice to have
• Eye catching photos that complement our message . I am not tied to the peach and cream color recommendation, but find those colors feminine but not so cliche as pinks and purples.
Should not have
• frilly design

```html
<!DOCTYPE html>
<html lang="en">
<head>
<meta charset="utf-8">
<title>Bright Path Functional Medicine – Brochure</title>
<link href="https://fonts.googleapis.com/css2?family=Playfair+Display:wght@400;700&family=Josefin+Sans:wght@400;600&family=Questrial&display=swap" rel="stylesheet">
<style>
:root{
  --sage:#a9bfc2;
  --sage-deep:#7fa2a0;
  --teal-dark:#4c706e;
  --slate:#4e6766;
  --tan:#e6cbb2;
  --tan-deep:#d9bb9c;
  --cream:#f5e6d9;
  --band:#b59e86;
  --brown:#9a7a5c;
  --ink:#4a4a48;
  --scene:#a9a9a9;
}
*{margin:0;padding:0;box-sizing:border-box}
html,body{width:1200px;height:2519px;overflow:hidden;background:#fff}
body{position:relative;font-family:"Questrial",sans-serif;color:var(--ink)}
.abs{position:absolute}
.spread{position:absolute;width:1078px;height:770px;overflow:hidden}
.spread-outside{left:70px;top:67px}
.spread-inside{left:74px;top:904px}
.panel{position:absolute;top:0;height:100%;width:360px}
.band-top{position:absolute;left:0;right:0;background:var(--band);opacity:.9}
.band-bottom{position:absolute;left:0;right:0;background:var(--sage-deep)}
.photo{position:absolute}
.serif-head{font-family:"Playfair Display",serif;font-weight:400;color:var(--slate);line-height:1.05}
.body{font-size:10.6px;line-height:12.2px}
.caps{font-family:"Josefin Sans",sans-serif;text-transform:uppercase;letter-spacing:1.2px;color:var(--brown)}
.aim-box{left:0;top:248px;width:338px;height:81px;border:1px solid #a38a72;border-left:none;padding:13px 0 0 35px;font-size:11.6px;line-height:16.5px;letter-spacing:.5px;color:#5a4a3c;white-space:nowrap;overflow:hidden}
.scene-bg{position:absolute;left:0;top:1743px;width:1200px;height:776px;background:var(--scene)}
.contact-item{position:absolute;left:0;width:360px;text-align:center;font-family:"Josefin Sans",sans-serif;font-size:7px;letter-spacing:.6px;text-transform:uppercase;color:var(--ink)}
.contact-item svg{display:block;margin:0 auto 6px}
</style>
</head>
<body>

<!-- Outside spread -->
<section class="spread spread-outside">
  <div class="panel" style="left:0;background:var(--sage)"></div>
  <div class="panel" style="left:360px;background:var(--tan)"></div>
  <div class="panel" style="left:720px;width:358px;background:var(--cream)"></div>
  <div class="band-top" style="top:26px;height:32px"></div>
  <div class="band-bottom" style="top:715px;height:28px"></div>

  <!-- back panel -->
  <h2 class="serif-head abs" style="left:37px;top:86px;font-size:16.5px;width:300px">What are your treatment protocols based on?</h2>
  <p class="body abs" style="left:37px;top:128px;width:292px">Treatment protocols are based on making you feel better with a focused wellness program that treats underlying cause. We want to optimize body systems by reducing inflammation, treating insulin resistance, improving catabolic physiology, and reducing oxidative stress. Treatment protocols are a combination of supplement support and hormone balance in addition to lifestyle optimization. Supplement programs tend to be focused and last approximately 6 months. Hormone programs continue for as long as you have symptoms. We will work together to determine what type of treatment program works best for you.</p>
  <div class="photo" role="img" aria-label="Photo of the clinic reception area with lounge seating" style="left:0;top:296px;width:325px;height:184px;background:linear-gradient(135deg,#5d5a57,#8a8580 45%,#c9c2b8 70%,#6a5c4c)"></div>
  <div class="abs" style="left:100px;top:501px;width:155px;height:30px;border:1px solid #6a7f80;font-family:'Josefin Sans',sans-serif;font-size:14px;letter-spacing:3.2px;text-align:center;line-height:31px;color:#3f4b4b">CONTACT US</div>
  <div class="contact-item" style="top:542px">
    <svg width="9" height="11" viewBox="0 0 9 11"><path d="M4.5 0A4 4 0 0 0 .5 4c0 3 4 7 4 7s4-4 4-7a4 4 0 0 0-4-4z" fill="#c49a74"/><circle cx="4.5" cy="4" r="1.5" fill="#a9bfc2"/></svg>Address</div>
  <div class="contact-item" style="top:582px">
    <svg width="10" height="10" viewBox="0 0 10 10"><path d="M2 0l2 2.5-1 1.3a6 6 0 0 0 3.2 3.2L7.5 6 10 8l-1.5 2C4 10 0 6 0 1.5z" fill="#c49a74"/></svg>+1 505 555 0142</div>
  <div class="contact-item" style="top:623px">
    <svg width="10" height="10" viewBox="0 0 10 10"><circle cx="5" cy="5" r="4.3" fill="none" stroke="#c49a74" stroke-width="1.2"/><path d="M.7 5h8.6M5 .7c-2.4 2.4-2.4 6.2 0 8.6M5 .7c2.4 2.4 2.4 6.2 0 8.6" stroke="#c49a74" stroke-width=".9" fill="none"/></svg>brightpath.example</div>
  <div class="contact-item" style="top:664px">
    <svg width="11" height="8" viewBox="0 0 11 8"><rect width="11" height="8" fill="#c49a74"/><path d="M0 0l5.5 4.5L11 0" stroke="#a9bfc2" fill="none"/></svg>hello@brightpath.example</div>

  <!-- inside flap: doctor -->
  <div class="abs" style="left:408px;top:0;width:262px;height:285px;border:1px solid #a38a72;border-top:none"></div>
  <div class="photo" role="img" aria-label="Family portrait of the medical director with her family seated outdoors on grass" style="left:428px;top:0;width:222px;height:265px;background:linear-gradient(180deg,#7c6a52,#5d6b3c 55%,#3f5230)"></div>
  <div class="abs" style="left:360px;top:303px;width:360px;text-align:center">
    <div><span class="caps" style="font-size:10px;letter-spacing:.5px;color:var(--slate)">Meet</span> <span class="serif-head" style="font-size:34px;color:#b38b66">Dr. Elena</span></div>
    <div class="serif-head" style="font-size:47px;font-weight:700;margin-top:-2px">Varga</div>
    <div class="caps" style="font-size:10px;letter-spacing:3.4px;color:#3f4b4b;margin-top:9px">Medical Director</div>
  </div>
  <p class="abs" style="left:397px;top:427px;width:290px;font-size:11.2px;line-height:16.4px">Dr. Elena Varga was born and raised in New Mexico. She grew up in Espanola and attended the Rio Grande School of Medicine in Albuquerque. Dr. Varga completed her residency training in Obstetrics and Gynecology at St. Anselm Hospital in Houston, Texas, in 1996. Dr. Varga was extensively trained in advanced operative laparoscopy and hysteroscopy. Dr. Varga was in private practice at St. Clare Hospital in Dallas, Texas, for five years prior to making the decision to return home. She has practiced in Santa Fe since September 2000. Dr. Varga opened Mesa Rio Ob/Gyn in 2005 and takes extreme pride in being able to offer the latest in technology for minimally invasive treatments for her patients</p>

  <!-- cover -->
  <div class="abs" style="left:770px;top:58px;width:308px;height:243px;background:var(--sage)"></div>
  <div class="abs" style="left:770px;top:188px;width:308px;text-align:center">
    <div class="serif-head" style="font-size:48px;font-weight:700">Bright Path</div>
    <div class="caps" style="font-size:12px;letter-spacing:3.6px;color:var(--slate);margin-top:8px">Functional Medicine</div>
  </div>
  <div class="photo" role="img" aria-label="Portrait of a woman with short hair touching her neck, soft skin tones" style="left:720px;top:320px;width:358px;height:450px;background:radial-gradient(ellipse at 55% 40%,#e9c8ae 0%,#e4bfa3 35%,#f0ddcc 70%,#f5e6d9 100%)"></div>
  <div class="band-bottom" style="top:715px;height:28px;left:720px;opacity:.55"></div>
</section>

<!-- Inside spread -->
<section class="spread spread-inside">
  <div class="panel" style="left:0;background:var(--cream)"></div>
  <div class="panel" style="left:360px;width:359px;background:var(--sage)"></div>
  <div class="panel" style="left:719px;width:359px;background:var(--cream)"></div>
  <div class="band-top" style="top:28px;height:30px"></div>
  <div class="band-bottom" style="top:714px;height:28px"></div>

  <!-- left -->
  <div class="photo" role="img" aria-label="Photo of a woman relaxing during a facial treatment" style="left:31px;top:39px;width:329px;height:191px;background:linear-gradient(120deg,#9fc3cf,#d7e4e8 45%,#e8d2c2 70%,#f1efee)"></div>
  <div class="abs caps aim-box">Functional medicine’s aim is to heal<br>the physical body in order to engage<br>in our life purpose of connection and<br>emotional and spiritual growth.</div>
  <p class="abs" style="left:36px;top:344px;width:292px;font-size:11.2px;line-height:13.6px"><b>Dr. Elena Varga</b> specializes in women’s health and has over 25 years of experience. She is an expert in bio-identical hormone replacement therapy and has been a Dermavita bio-identical hormone pellet practitioner for over 10 years. Dr. Varga has been practicing functional medicine for many years with a primary focus on hormone therapy, medical weight loss, and lifestyle change. She has recently expanded her practice to incorporate additional services including healing with a focus on adrenal, gastrointestinal and detoxification programs. Dr. Varga is a practitioner of the Hale Method for functional medicine and works closely with Dr. Marcus Hale as her mentor in the development of individual treatment protocols for our patients. Dr. Hale has over 25 years of experience in functional medicine.</p>
  <div class="abs" style="left:0;top:590px;width:440px;height:108px;background:var(--tan-deep);padding:14px 0 0 40px">
    <div class="caps" style="font-size:13px;line-height:16.5px;letter-spacing:.9px;color:#5a4a3c">What do patients’ have to say about their experience with Dr. Varga?</div>
    <p style="font-size:10px;line-height:10.6px;margin-top:2px;width:380px">Lorem ipsum dolor sit amet, consectetuer adipiscing elit, sed diam nonummy nibh euismod tincidunt ut laoreet dolore magna aliquam erat volutpat. Ut wisi enim ad minim veniam, quis nostrud exerci tation ullamcorper suscipit lobortis nisl ut aliquip ex ea commodo consequat. Duis autem vel eum iriure dolor in hendrerit in</p>
  </div>

  <!-- middle -->
  <h3 class="serif-head abs" style="left:384px;top:82px;width:300px;font-size:16.5px">Why should you consider a functional medicine visit?</h3>
  <p class="body abs" style="left:384px;top:124px;width:290px">You are tired of feeling tired. You can’t even focus on the future because you are so overwhelmed. The pain of being unable to think clearly and being too tired to exercise are your daily reality. Your life goals seem like too much to think about, you just have to get through today.</p>
  <h3 class="serif-head abs" style="left:384px;top:198px;width:300px;font-size:16.5px">Who else should consider a functional medicine visit?</h3>
  <p class="body abs" style="left:384px;top:240px;width:290px">You want to achieve OPTIMAL health with a personalized medicine approach. You are eating well, exercising and engaging in stress reducing activities such as meditation. You want to know how to minimize the effects of aging and are ready to take a proactive approach in getting to the highest level of health you can achieve.</p>
  <div class="abs" style="left:384px;top:332px;width:335px;height:30px;background:var(--teal-dark);font-family:'Playfair Display',serif;font-weight:700;font-size:15px;letter-spacing:.5px;color:#f2ece4;line-height:30px;padding-left:8px">WHAT SYMPTOMS DO WE TREAT?</div>
  <div class="abs caps" style="left:384px;top:374px;font-size:15px">Weight Gain</div>
  <p class="body abs" style="left:384px;top:398px;width:290px">Adrenal dysfunction results in cortisol imbalance. The major function of cortisol is to help balance blood sugar. When cortisol is out of balance, your body will store body fat rather than burning fat for fuel resulting in weight gain. Menopausal hormone imbalance will also result in abdominal weight gain.</p>
  <div class="abs caps" style="left:384px;top:474px;font-size:15px">Fatigue</div>
  <p class="body abs" style="left:384px;top:497px;width:290px">Adrenal exhaustion results from long term stress that depletes cortisol. Testing and correcting cortisol will improve energy levels. Long term stress can result in mitochondrial dysfunction and organic acid tests can tell us how to support your mitochondria.</p>

  <!-- right -->
  <div class="abs caps" style="left:751px;top:82px;font-size:15px">Depression</div>
  <p class="body abs" style="left:751px;top:106px;width:292px">Adrenal exhaustion results from long term stress that depletes cortisol. Testing and correcting cortisol will improve energy levels. Long term stress can result in mitochondrial dysfunction and organic acid tests can tell us how to support your mitochondria.</p>
  <div class="abs caps" style="left:751px;top:182px;font-size:15px">Female Hormone Imbalance</div>
  <p class="body abs" style="left:751px;top:206px;width:292px">Optimizing hormonal balance is our specialty. We focus on optimizing hormone levels with bio-identical hormones, but also know that adrenal treatment protocols can improve symptoms of hot flashes, nights sweats, and foggy thinking.</p>
  <div class="abs caps" style="left:751px;top:272px;font-size:15px">GI Problems</div>
  <p class="body abs" style="left:751px;top:296px;width:292px">The immune cells that line our digestive tract are regulated by cortisol. Cortisol imbalance results in inflammation and “leaky gut” causing digestive symptoms like bloating, heartburn, constipation, or diarrhea. Utilizing a comprehensive program that includes avoiding inflammatory foods and GutView stool testing allow us to find underlying infections or sources of inflammation and allow us to develop a focused treatment plan.</p>
  <h3 class="serif-head abs" style="left:749px;top:406px;font-size:16.5px">What can I expect from my first visit?</h3>
  <p class="body abs" style="left:751px;top:432px;width:292px">During your initial consultation, we want to get to know each other and find out your expectations for health. We will explore your health history and symptoms as well as lifestyle factors including diet and sleep. We will discuss your goals and reasons for getting healthy. We know that we must incorporate lifestyle changes including stress reduction, diet and exercise optimization in any program for healing. We will discuss testing recommendations including blood work, hormone evaluation, cortisol, GI, and organic acid tests as well as nutritional and personal coaching options.</p>

  <!-- photo strip -->
  <div class="photo" role="img" aria-label="Photo of a woman in a towel wrap touching her face" style="left:473px;top:576px;width:216px;height:156px;background:linear-gradient(90deg,#4a3a30,#b59a86 45%,#ece6e2)"></div>
  <div class="photo" role="img" aria-label="Photo of a woman with raised arms in a field" style="left:689px;top:576px;width:185px;height:156px;background:linear-gradient(180deg,#cfcac4,#a7a098 60%,#8a8179)"></div>
  <div class="photo" role="img" aria-label="Photo of a woman touching her cheek beside a mirror" style="left:874px;top:576px;width:204px;height:156px;background:linear-gradient(90deg,#f1f2f2,#e6ddd6 50%,#d9cbbf)"></div>
</section>

<div class="scene-bg"></div>
</body>
</html>
```